Educational non-profit needs an End of the Year Flyer

We need a flyer to mail to our supporters asking for donations to our program. Hillcrest Open Learning Hub runs after school programs for low-income students in Pasadena, CA. This is our end of the year mailing to supporters asking them to finish out the year with their contributions so that we can meet our budget.

Target Market(s)

Donors and supporters of organization

Industry/Entity Type

Non-Profit

Font styles to use
Serif

Colors

Designer to choose colors to be used in the design.

Requirements
Must have
• The project should fit on a 6x9" card, and be printed on front and back. It should show pictures, use the copy I have included, a space for a label address, a stamp, and the return address.
Nice to have
• eye-catching, fun

```html
<!DOCTYPE html>
<html lang="en">
<head>
<meta charset="utf-8">
<title>Hillcrest Open Learning Hub – Year-End Appeal Card</title>
<link rel="stylesheet" href="https://fonts.googleapis.com/css2?family=Arimo:wght@400;700&family=Open+Sans:ital,wdth,wght@0,75..100,300..800;1,75..100,300..800&family=Courgette&display=swap">
<style>
  :root{
    --bg:#e6e4e1;
    --white:#ffffff;
    --red:#ea3a24;
    --orange:#f0592a;
    --yellow:#f6b727;
    --ink:#3b3b3b;
    --photo-warm:#7a5a48;
    --photo-dark:#2d2a35;
    --rule:#bdbdbd;
  }
  *{box-sizing:border-box;margin:0;padding:0}
  html,body{width:935px;height:1200px;overflow:hidden;background:var(--bg)}
  .canvas{position:relative;width:935px;height:1200px}
  .card{position:absolute;left:77px;width:780px;height:520px;background:var(--white);overflow:hidden;box-shadow:0 2px 8px rgba(0,0,0,.18)}
  .card--front{top:50px}
  .card--back{top:630px}
  .card svg.art{position:absolute;left:0;top:0}

  .org-name{position:absolute;font-family:"Open Sans",sans-serif;font-weight:700;color:var(--ink);text-align:center;line-height:1.2;display:flex;flex-direction:column;align-items:center;gap:8px}
  .org-name .mark{width:22px;height:22px;border-radius:50%;background:var(--yellow)}
  .card--front .org-name{left:20px;top:340px;width:150px;font-size:16px}
  .card--back .org-name{left:620px;top:380px;width:140px;font-size:14px}

  .headline{position:absolute;left:196px;top:302px;font-family:Arimo,sans-serif;font-weight:700;font-size:26.5px;color:var(--red);white-space:nowrap}
  .intro{position:absolute;left:196px;top:343px;width:570px;font-family:Arimo,sans-serif;font-weight:700;font-size:13.6px;line-height:19px;color:var(--ink)}
  .link-row{position:absolute;left:196px;top:390px;display:flex;align-items:center;gap:8px;font-family:"Open Sans",sans-serif;font-size:13.5px;color:var(--ink)}
  .pill{display:inline-block;border-radius:14px;padding:3px 20px;font-family:"Open Sans",sans-serif;font-weight:700;letter-spacing:1px;color:var(--white);box-shadow:2px 2px 3px rgba(0,0,0,.25)}
  .pill--yellow{background:var(--yellow);font-size:15px}
  .pill--orange{background:var(--orange);font-size:15px}
  .greeting{font-family:Courgette,cursive;color:var(--yellow);font-size:20px;white-space:nowrap}
  .card--front .greeting{position:absolute;left:196px;top:426px}
  .contact-band{position:absolute;left:170px;top:463px;width:610px;height:41px;background:var(--orange);border-radius:14px 0 0 14px;display:flex;align-items:center;justify-content:space-between;padding:0 22px 0 24px;color:var(--white);font-family:"Open Sans",sans-serif}
  .contact-band .address{font-size:16px}
  .phone{display:flex;align-items:center;gap:8px;font-family:"Open Sans",sans-serif;font-weight:600;font-size:22px;letter-spacing:1px}
  .phone svg{width:20px;height:20px}

  .appeal{position:absolute;left:0;top:205px;width:395px;height:233px;background:var(--yellow);padding:12px 22px 0 22px}
  .appeal .appeal-greeting{font-family:Courgette,cursive;color:var(--red);font-size:19px;white-space:nowrap}
  .appeal .appeal-copy{margin-top:5px;font-family:"Open Sans",sans-serif;font-stretch:75%;font-size:11.6px;line-height:15.6px;color:var(--white);letter-spacing:-.3px}
  .appeal .link-label{margin-top:10px;font-family:"Open Sans",sans-serif;font-size:12.5px;color:var(--red)}
  .appeal .pill{margin-top:3px}
  .back-band{position:absolute;left:0;top:447px;width:404px;height:73px;background:var(--orange);padding:10px 22px;color:var(--white);font-family:"Open Sans",sans-serif}
  .back-band .social{font-style:italic;font-size:13.5px;margin-top:4px;white-space:nowrap}
  .return-address{position:absolute;left:496px;top:55px;font-family:"Open Sans",sans-serif;font-style:normal;font-size:15px;line-height:20px;color:var(--ink)}
  .stamp-box{position:absolute;left:667px;top:35px;width:95px;height:64px;border:1.5px solid var(--rule)}
  .address-line{position:absolute;left:458px;width:304px;height:0;border-top:1.5px solid var(--rule)}
</style>
</head>
<body>
<div class="canvas">

  <!-- FRONT -->
  <section class="card card--front">
    <svg class="art" width="780" height="300" viewBox="0 0 780 300">
      <defs>
        <linearGradient id="frontPhoto" x1="0" y1="0" x2="1" y2="1">
          <stop offset="0" stop-color="#a07a5f"/>
          <stop offset="0.5" stop-color="#7a5a48"/>
          <stop offset="1" stop-color="#2d2a35"/>
        </linearGradient>
      </defs>
      <path d="M0 150 C100 205 240 270 380 276 C520 280 700 210 780 90 V130 C700 230 560 282 420 285 C260 287 120 255 0 222 Z" fill="var(--yellow)"/>
      <path d="M780 110 C700 220 560 281 420 285 C560 287 700 262 780 240 Z" fill="var(--orange)"/>
      <path d="M0 226 C150 264 300 284 420 287" fill="none" stroke="var(--orange)" stroke-width="3"/>
      <path d="M0 0 H780 V13 C700 170 520 272 380 272 C240 272 100 215 0 165 Z" fill="url(#frontPhoto)" role="img" aria-label="Photo of smiling children from the afterschool program holding basketballs in a gym"/>
      <path d="M780 13 C700 170 520 272 380 272" fill="none" stroke="var(--white)" stroke-width="3"/>
    </svg>

    <div class="org-name"><span class="mark"></span>Hillcrest Open Learning Hub</div>

    <h1 class="headline">We need your help to finish out 2018 strong!</h1>
    <p class="intro">We have had a wonderful 25th year of serving the children and families of Pasadena here at Hillcrest Open Learning Hub with high quality afterschool programs.</p>
    <div class="link-row">Just look for the link on our website <span class="pill pill--yellow">www.brightstepkids.org</span></div>
    <p class="greeting">Merry Christmas from all of us at HOLH!</p>

    <div class="contact-band">
      <span class="address">418 N. Larkmoor Ave. Pasadena, CA&nbsp; 91106</span>
      <span class="phone">
        <svg viewBox="0 0 24 24"><circle cx="12" cy="12" r="10.5" fill="none" stroke="#fff" stroke-width="2"/><path d="M8.6 6.8c.5-.4 1.1-.3 1.4.2l1 1.6c.3.5.2 1-.2 1.3l-.7.5c.5 1.3 1.4 2.3 2.7 2.9l.5-.7c.3-.4.9-.5 1.3-.2l1.6 1c.5.3.6.9.2 1.4l-.7.8c-.6.6-1.5.8-2.3.4-2.5-1.1-4.5-3.1-5.6-5.6-.3-.8-.2-1.7.4-2.3z" fill="#fff"/></svg>
        (626) 555-0147
      </span>
    </div>
  </section>

  <!-- BACK -->
  <section class="card card--back">
    <svg class="art" width="780" height="520" viewBox="0 0 780 520">
      <defs>
        <linearGradient id="backPhoto" x1="0" y1="0" x2="1" y2="1">
          <stop offset="0" stop-color="#6f5a4c"/>
          <stop offset="0.6" stop-color="#3c3440"/>
          <stop offset="1" stop-color="#5c4a3e"/>
        </linearGradient>
      </defs>
      <path d="M0 0 H492 C458 50 432 120 414 189 H0 Z" fill="url(#backPhoto)" role="img" aria-label="Group photo of students from the afterschool club gathered in a restaurant"/>
      <path d="M504 0 H522 C462 100 420 250 410 520 H398 C402 250 446 100 504 0 Z" fill="var(--orange)"/>
    </svg>

    <div class="appeal">
      <p class="appeal-greeting">Merry Christmas from all of us at HOLH!</p>
      <p class="appeal-copy">We need your help to finish out 2018 strong! We have had a wonderful 25th year of serving the children and families of Pasadena here at Hillcrest Open Learning Hub with high quality afterschool programs. Hundreds and hundreds of students have been a part of the Bright Step Kids Club family. Our annual budget is $275,000 and we count on $100,000 from individual donors. Will you join with us for an end of the year contribution? Remember, you can give online through GiveSwift.</p>
      <p class="link-label">Just look for the link on our website</p>
      <span class="pill pill--orange">www.brightstepkids.org</span>
    </div>

    <div class="back-band">
      <span class="phone">
        <svg viewBox="0 0 24 24"><circle cx="12" cy="12" r="10.5" fill="none" stroke="#fff" stroke-width="2"/><path d="M8.6 6.8c.5-.4 1.1-.3 1.4.2l1 1.6c.3.5.2 1-.2 1.3l-.7.5c.5 1.3 1.4 2.3 2.7 2.9l.5-.7c.3-.4.9-.5 1.3-.2l1.6 1c.5.3.6.9.2 1.4l-.7.8c-.6.6-1.5.8-2.3.4-2.5-1.1-4.5-3.1-5.6-5.6-.3-.8-.2-1.7.4-2.3z" fill="#fff"/></svg>
        (626) 555-0147
      </span>
      <p class="social">Visit us on Friendline - Hillcrest Open Learning Hub</p>
    </div>

    <address class="return-address">418 N. Larkmoor Ave.<br>Pasadena, CA&nbsp; 91106</address>
    <div class="stamp-box"></div>
    <div class="address-line" style="top:210px"></div>
    <div class="address-line" style="top:249px"></div>
    <div class="address-line" style="top:288px"></div>
    <div class="address-line" style="top:326px"></div>

    <div class="org-name"><span class="mark"></span>Hillcrest Open Learning Hub</div>
  </section>

</div>
</body>
</html>
```